Flyer Design - You Need a Mobile Website

We need an A4 size flyer design for print to be used as part of a Direct Mail package.

The target audience is small business owners, such as Vets, Dentists, Plumbers and others who would benefit from owning a Mobile Website.

"You're not fully open for business until you have a mobile website." is the theme.

Our product is a mobile-phone/smartphone optimized version of the client's normal desktop website, automatically updated as the main web-site is changed.

The desired course of action is for the reader to go to the website and order a FREE preview.

IMPORTANT NOTE: 4-9-2013 we have revieds some of the wording see File4 "Get your Mobile Website Built Free of charge"

Target Market(s)

Small Business Owners, businesses that provide emergency/urgent services. (eg Vets, Dentist, Plumber etc)

Industry/Entity Type

Small Business

Requirements
Must have
• Design must comply with the printers specification for A4 flyers, details are here: http://www.printvarolo.com.au/Templates/A4Templates/tabid/142/default.aspx
(Photoshop version is attached)

Proposed Text is attached (see attachment 1 "You're not fully open for business until you have a mobile website")
Nice to have
• Further background explanation is attached. (see attachment 2 "Brindlecove Mobile Websites Flyer-Explanation")

```html
<!DOCTYPE html>
<html lang="en">
<head>
<meta charset="utf-8">
<title>You're Not Fully Open For Business – Brindlecove Mobile Websites</title>
<link href="https://fonts.googleapis.com/css2?family=Open+Sans:wght@300;400;600;700&display=swap" rel="stylesheet">
<style>
:root{
  --sky:#3b78c0;
  --frame:#e9e9ea;
  --orange:#f26522;
  --rust:#6b2a10;
  --rule:#8a8a8a;
  --ink:#333;
  --ink-soft:#555;
  --tab-blue:#2e86c8;
  --link-blue:#3d8fc4;
  --teal-link:#2a8aa8;
  --panel-grey:#ededed;
  --cream:#fff1c8;
  --ice:#d3ebf3;
  --white:#fff;
}
*{box-sizing:border-box;margin:0;padding:0}
html,body{width:855px;height:1200px;overflow:hidden}
body{background:var(--sky);font-family:"Open Sans",Arial,sans-serif;color:var(--ink);position:relative}
.handset{position:absolute;left:24px;top:24px;width:805px;height:1152px;background:var(--frame);border-radius:130px}
.speaker-slot{position:absolute;left:342px;top:71px;width:164px;height:20px;background:var(--white);border-radius:10px;border:1px solid #bbb}
.home-key{position:absolute;left:370px;top:1103px;width:111px;height:43px;background:var(--white);border-radius:8px;box-shadow:1px 2px 2px #aaa}
.screen{position:absolute;left:24px;top:130px;width:805px}
.headline{background:var(--orange);border-top:5px solid var(--rust);border-bottom:5px solid var(--rule);height:123px;color:var(--white);text-align:center;padding-top:22px}
.headline .kicker{font-weight:300;font-size:25px;letter-spacing:.3px;line-height:1.2}
.headline .main{font-weight:700;font-size:39px;line-height:1.2}
.intro{background:var(--white);height:277px;position:relative}
.intro p{position:absolute;left:38px;width:510px;font-size:15px;line-height:20px;color:#444}
.intro .lead{top:35px}
.intro .year{top:110px}
.preview{position:absolute;left:536px;top:16px;width:272px;height:188px}
.phone-shot{position:absolute;top:0;width:82px;height:160px;border-radius:12px;background:linear-gradient(#1c1c1c,#3a3a3a);padding:16px 5px 22px}
.phone-shot .glass{width:100%;height:100%;background:linear-gradient(#f5f7ee,#c9d88f 30%,#f2f2ea 32%,#fff)}
.phone-shot.not{left:60px}.phone-shot.yes{left:157px}
.bubble{position:absolute;background:var(--white);border:2px solid #222;border-radius:50%;font-weight:700;font-size:11px;line-height:11px;text-align:center;padding:7px 8px}
.bubble.not{left:28px;top:8px;transform:rotate(-15deg)}
.bubble.yes{left:204px;top:10px;transform:rotate(12deg)}
.preview .caption{position:absolute;left:0;top:170px;width:272px;font-size:6px;font-weight:700;text-align:center;color:#222}
.stats{position:absolute;top:218px;left:38px;display:flex;align-items:center}
.stat{display:flex;align-items:center;margin-right:20px}
.stat b{font-weight:400;color:var(--orange);font-size:29px;margin-right:10px}
.stat span{font-size:12.5px;line-height:17px;color:#444}
.reasons{background:var(--panel-grey);height:171px;position:relative;border-bottom:4px solid #ddd}
.reasons .tab{position:absolute;left:228px;top:-3px;width:342px;height:50px;background:var(--tab-blue);color:var(--white);font-size:19px;text-align:center;line-height:50px}
.reason{position:absolute;font-size:13px;color:#444;display:flex;align-items:center}
.reason svg{width:18px;height:18px;margin-right:9px}
.footnote{position:absolute;left:100px;top:145px;font-size:8.5px;color:#555}
.compare{display:flex;height:192px}
.compare .col{flex:none;padding-top:24px}
.compare .standard{width:393px;background:var(--cream);padding-left:88px}
.compare .mobile{width:412px;background:var(--ice);padding-left:74px}
.compare h3{font-weight:400;font-size:12.5px;margin-bottom:17px}
.standard h3{color:var(--orange)}.mobile h3{color:var(--link-blue)}
.compare ul{list-style:none;font-size:12.5px;line-height:16.8px;color:#444}
.compare li{position:relative;padding-left:13px}
.compare li::before{content:"•";position:absolute;left:0;color:#888}
.mobile ul{margin-top:-4px}
.cta{background:var(--white);height:48px;text-align:center;font-weight:700;font-size:26px;line-height:48px;color:var(--ink-soft)}
.cta em{font-style:normal;color:var(--orange)}
.order{background:var(--cream);border-top:4px solid #ddd;border-bottom:4px solid #c9c9c9;height:142px;position:relative;font-size:12.5px;line-height:18.5px}
.order .how{position:absolute;left:25px;top:18px;font-weight:600;color:#111}
.order .how a{color:var(--teal-link);font-weight:400;text-decoration:none}
.order .how em{font-style:normal;color:var(--orange)}
.order .company{position:absolute;right:25px;top:16px;text-align:right;color:#222}
.order .company strong{font-size:15.5px;font-weight:700;display:block;line-height:22px}
.order .company .mail{color:var(--teal-link)}
</style>
</head>
<body>
<div class="handset">
  <div class="speaker-slot"></div>
  <div class="home-key"></div>
</div>

<main class="screen">
  <header class="headline">
    <div class="kicker">YOU'RE NOT FULLY OPEN FOR BUSINESS</div>
    <div class="main">UNTIL YOU HAVE A MOBILE WEBSITE.</div>
  </header>

  <section class="intro">
    <p class="lead">More than half of all Australians are using their mobile phones to access the web. That means that half of your customers are too. Now, all businesses need a Mobile Website just to keep up with their competitors.</p>
    <p class="year">In 2012 Australian Smartphone users accessed the internet:</p>
    <div class="preview">
      <div class="phone-shot not"><div class="glass" role="img" aria-label="Desktop version of a sample clinic site shrunk onto a phone screen"></div></div>
      <div class="phone-shot yes"><div class="glass" role="img" aria-label="Mobile version of a sample clinic site with large green buttons"></div></div>
      <div class="bubble not">Not<br>Mobile</div>
      <div class="bubble yes">Mobile!</div>
      <div class="caption">Keep your colors simple. A white background makes your site's buttons pop!</div>
    </div>
    <div class="stats">
      <div class="stat"><b>62%</b><span>looked for information<br>on products and services</span></div>
      <div class="stat"><b>55%</b><span>looked for suppliers<br>of products or services</span></div>
      <div class="stat"><b>33%</b><span>ordered goods or services</span></div>
    </div>
  </section>

  <section class="reasons">
    <div class="tab">WHY GET A MOBILE WEBITE?</div>
    <div class="reason" style="left:74px;top:66px"><svg viewBox="0 0 18 18"><rect x="1" y="1" width="16" height="16" fill="#fde6b0" stroke="#e08a2a"/><path d="M2 15 L7 9 L10 11 L16 3" stroke="#d9531e" stroke-width="2" fill="none"/></svg>To get more website traffic*.</div>
    <div class="reason" style="left:301px;top:66px"><svg viewBox="0 0 18 18"><circle cx="9" cy="9" r="8" fill="#f6b21b"/><path d="M5 13 L12 6" stroke="#d9311e" stroke-width="2"/></svg>To Boost your brand</div>
    <div class="reason" style="left:549px;top:62px"><svg viewBox="0 0 18 24" style="height:26px"><path d="M1 2h16M4 2 L9 12 L14 2M9 12v10M6 22h6" stroke="#2f4f86" stroke-width="2.4" fill="none"/></svg>To Generate new leads</div>
    <div class="reason" style="left:74px;top:98px"><svg viewBox="0 0 18 18"><rect x="1" y="11" width="4" height="6" fill="#f26522"/><rect x="7" y="7" width="4" height="10" fill="#f6b21b"/><rect x="13" y="2" width="4" height="15" fill="#4caf3f"/></svg>To Increase sales and revenue.</div>
    <div class="reason" style="left:301px;top:98px"><svg viewBox="0 0 18 18"><circle cx="7" cy="9" r="6" fill="#e3241b"/><path d="M14 5l3-2M14 9h4M14 13l3 2" stroke="#e3241b" stroke-width="1.5"/></svg>To avoid frustrating your audience</div>
    <div class="reason" style="left:549px;top:98px"><svg viewBox="0 0 18 18"><rect x="1" y="2" width="7" height="7" fill="#e3241b"/><rect x="10" y="10" width="7" height="7" fill="#2fa84f"/></svg>To step into the digital age</div>
    <div class="reason" style="left:74px;top:127px"><svg viewBox="0 0 18 24" style="height:26px"><path d="M5 2 L8 12 M13 2 L10 12 M5 13h9v6a4 4 0 0 1-9 0z" stroke="#c8202a" stroke-width="1.6" fill="none"/></svg>To stay ahead of the competition</div>
    <div class="footnote">(*Adding a mobile friendly site results in an overall traffic increase of 18% (source: Marlowe Research)</div>
  </section>

  <section class="compare">
    <div class="col standard">
      <h3>STANDARD WEBSITE</h3>
      <ul>
        <li>Text is too small.</li>
        <li>Must Pinch, zoom and scroll to read.</li>
        <li>Links are too small for touch navigation</li>
      </ul>
    </div>
    <div class="col mobile">
      <h3>MOBILE WEBSITE</h3>
      <ul>
        <li>Finger friendly navigation easy too use</li>
        <li>Click to call button, makes it easy for customers to contact you directly</li>
        <li>Mobile maps with find us button</li>
        <li>Automatically updates when you change your regular website</li>
        <li>Works on All Smartphones</li>
      </ul>
    </div>
  </section>

  <div class="cta">GET A MOBILE WEBSITE <em>FREE PREVIEW NOW!</em></div>

  <section class="order">
    <div class="how">
      GO TO<br>
      <a href="http://www.brindlecove.com.au/offer">http://www.brindlecove.com.au/offer</a><br>
      to order you new Mobile Website Preview.<br>
      Within a few hours Brindlecove will build your new Mobile Website ready<br>
      for you to Preview; <em>Totally FREE to you. (Normally $199 value)</em>
    </div>
    <address class="company" style="font-style:normal">
      <strong>BRINDLECOVE CORPORATION Pty Ltd</strong>
      Established 1999.<br>
      Level 4, 58 Harlow Lane Melbourne –<br>
      P.O. Box 742 Kelsworth Victoria 3107<br>
      PHONE: 03 9000 4417<br>
      <span class="mail">Email: admin@brindlecove.com.au</span>
    </address>
  </section>
</main>
</body>
</html>
```